Young Accounting firm needing a captivating business card

We need a business card design that forces the person to look at the card because its either gold foil, plastic, or lettering pop up etc. We already have a logo with a specific gold color and we need to make it pop. We are an accounting firm. I need the words" accounting, payroll, licenses, audits, taxes" somewhere on the business card so as to describe what we do- preferably on the side where the logo is at.

Industry/Entity Type

Accounting

Contact Information for Business Card

Address 48276 9th Ave S Ste 305, Federal Way, WA 98117
Business Phone (360)418-2096
Fax (360)418-2157
Office Cell Phone (360)586-7319

Font styles to use
Serif

Colors
85abd2

Requirements
Must have
• It should state
• "Accounting" "Taxes" "Audits" "Licenses" "Payroll"
Nice to have
• Matte with gold foil, different textures, With Either a textured ivory background or gray blue slate background
Should not have
• colorful colors

```html
<!DOCTYPE html>
<html lang="en">
<head>
<meta charset="utf-8">
<title>Ledgerline Business Card</title>
<link href="https://fonts.googleapis.com/css2?family=Open+Sans:wght@400;600&display=swap" rel="stylesheet">
<style>
  :root {
    --gold: #b58d12;
    --gold-faint: rgba(226, 206, 140, 0.28);
    --card: #ffffff;
    --facet: #eef1f6;
    --facet-deep: #e4e8f0;
    --stage: #e9e6e1;
  }
  * { margin: 0; padding: 0; box-sizing: border-box; }
  html, body { width: 1200px; height: 800px; overflow: hidden; }
  body {
    background: var(--stage);
    font-family: "Open Sans", Arial, sans-serif;
    color: var(--gold);
    display: flex;
    flex-direction: column;
    align-items: center;
    justify-content: center;
    gap: 56px;
  }
  .card {
    position: relative;
    width: 525px;
    height: 300px;
    background: var(--card);
    box-shadow: 0 6px 18px rgba(0,0,0,0.12);
    overflow: hidden;
  }
  .card-facets { position: absolute; inset: 0; width: 100%; height: 100%; }
  .brand {
    position: absolute;
    display: flex;
    align-items: center;
    gap: 10px;
    font-weight: 600;
    font-size: 34px;
    letter-spacing: -0.5px;
    color: var(--gold);
  }
  .brand-mark { width: 30px; height: 30px; background: var(--gold); }
  .brand-front { right: 36px; top: 120px; }
  .brand-back { right: 30px; top: 168px; font-size: 30px; }
  .brand-back .brand-mark { width: 26px; height: 26px; }
  .services {
    position: absolute;
    left: 44px;
    top: 92px;
    list-style: none;
    font-weight: 600;
    font-size: 21px;
    line-height: 1.22;
  }
  .services li::before { content: "•"; margin-right: 12px; }
  .person { position: absolute; left: 36px; top: 34px; }
  .person-name { font-weight: 600; font-size: 28px; line-height: 1.1; }
  .person-role { font-size: 12px; letter-spacing: 1.5px; margin-top: 2px; }
  .contacts {
    position: absolute;
    left: 36px;
    top: 130px;
    list-style: none;
    font-size: 14px;
    line-height: 1.7;
  }
  .contacts li { display: flex; align-items: center; gap: 9px; }
  .contacts svg { width: 14px; height: 14px; fill: var(--gold); flex: none; }
</style>
</head>
<body>

<section class="card card-front">
  <svg class="card-facets" viewBox="0 0 525 300" preserveAspectRatio="none" aria-hidden="true">
    <polygon points="0,300 0,120 260,300" fill="var(--facet)"/>
    <polygon points="300,0 525,0 525,150" fill="var(--facet)"/>
    <polygon points="150,300 525,170 525,300" fill="var(--facet-deep)" opacity="0.5"/>
    <rect x="210" y="40" width="200" height="200" fill="var(--gold-faint)"/>
  </svg>
  <ul class="services">
    <li>Accounting</li>
    <li>Taxes</li>
    <li>Audits</li>
    <li>Licenses</li>
    <li>Payroll</li>
  </ul>
  <div class="brand brand-front"><span class="brand-mark"></span>Ledgerline</div>
</section>

<section class="card card-back">
  <svg class="card-facets" viewBox="0 0 525 300" preserveAspectRatio="none" aria-hidden="true">
    <polygon points="0,0 200,0 0,150" fill="var(--facet)"/>
    <polygon points="170,300 525,210 525,300" fill="var(--facet-deep)" opacity="0.6"/>
    <rect x="250" y="60" width="190" height="190" fill="var(--gold-faint)"/>
  </svg>
  <div class="person">
    <p class="person-name">Daniel Hart</p>
    <p class="person-role">MANAGER</p>
  </div>
  <ul class="contacts">
    <li><svg viewBox="0 0 14 14"><path d="M4 0h6a1 1 0 0 1 1 1v12a1 1 0 0 1-1 1H4a1 1 0 0 1-1-1V1a1 1 0 0 1 1-1zm0 2v9h6V2z"/></svg>(360)418-2096</li>
    <li><svg viewBox="0 0 14 14"><path d="M3 0h8v4H3zM1 5h12v6h-2v3H3v-3H1zm3 4v4h6V9z"/></svg>(360)418-2157</li>
    <li><svg viewBox="0 0 14 14"><path d="M3 0l3 3-2 2c1 2 3 4 5 5l2-2 3 3-2 3C6 13 1 8 0 3z"/></svg>(360)586-7319</li>
    <li><svg viewBox="0 0 14 14"><path d="M0 2h14v10H0zm1 1v.5l6 4 6-4V3z"/></svg>daniel@ledgerlinetax.com</li>
    <li><svg viewBox="0 0 14 14"><path d="M7 0a5 5 0 0 1 5 5c0 4-5 9-5 9S2 9 2 5a5 5 0 0 1 5-5zm0 3a2 2 0 1 0 0 4 2 2 0 0 0 0-4z"/></svg>48276 9th Ave S Ste 305, Federal Way, WA 98117</li>
  </ul>
  <div class="brand brand-back"><span class="brand-mark"></span>Ledgerline</div>
</section>

</body>
</html>
```